High Quality Outdoor Extension Cord Sleeve/Packaging

-Files proved are for reference only! I want a new fresh design. Do not just copy their design.
-This is a sleeve that will slide over the maroon extension cord. The cord will show with the packaging over it. So the color pallet must look good with the maroon-colored cord.
-Design packaging to fit the attached dieline file.
-Copy all textual information from the file "TEXT INFO".
-File "EXAMPLE", is another packaging design to reference as a guide.
-File "Maroon Ai" is our business logo to use.
-File "Cord" are images of the extension cord this sleeve will go over.

-Up to you whether or not you use the graphic emojis from the file "TEXT INFO"

Target Market(s)

Men 30-65

Industry/Entity Type

Construction/Home Projects/Lawn and Garden

Requirements
Must have
• "Made in America" or "Made in the USA" with an American flag icon or image. Our logo on packaging.

```html
<!DOCTYPE html>
<html lang="en">
<head>
<meta charset="utf-8">
<title>Voltline Cable – Outdoor Lighted Extension Cord Sleeve</title>
<link href="https://fonts.googleapis.com/css2?family=Oswald:wght@600;700&family=Roboto:ital,wght@0,400;0,700;0,900;1,400&family=Work+Sans:wght@400;600&display=swap" rel="stylesheet">
<style>
:root{
  --cord-red:#c8352c;
  --band-red:#d9442f;
  --band-red-light:#e2624a;
  --silver-light:#f4f4f4;
  --silver-mid:#cfcfcf;
  --ink:#000;
  --paper:#fff;
  --signal-yellow:#fcd006;
  --feature-red:#e2231a;
  --guide-red:#e52420;
  --guide-blue:#28298a;
  --flag-red:#b22234;
  --flag-blue:#3c3b6e;
}
*{margin:0;padding:0;box-sizing:border-box}
html,body{width:733px;height:1200px;overflow:hidden;background:var(--paper)}
.sleeve{position:relative;width:733px;height:1200px;font-family:"Roboto",sans-serif;color:var(--paper)}
.abs{position:absolute}
.cord-photo{position:absolute;background:radial-gradient(ellipse at center,#e25a4c 0%,#c8352c 55%,#8e1f1a 100%)}
.cord-photo.top{left:25px;top:0;width:400px;height:128px;border-radius:200px 200px 0 0}
.cord-photo.bottom{left:20px;top:1057px;width:445px;height:140px;border-radius:0 0 220px 220px}
.silver-band{left:0;top:140px;width:733px;height:95px;background:linear-gradient(180deg,#bdbdbd 0%,var(--silver-light) 35%,var(--silver-mid) 100%)}
.guide-blue{height:1px;background:var(--guide-blue);left:0;width:733px}
.guide-fold{left:438px;width:0;border-left:1.5px dashed var(--guide-red)}
.brand{display:flex;align-items:center;gap:6px;justify-content:center;width:200px;color:#222;font-family:"Oswald",sans-serif;font-weight:700;font-size:20px;letter-spacing:2px}
.brand-dot{width:14px;height:14px;border-radius:50%;background:var(--cord-red)}
.red-band{background:linear-gradient(180deg,var(--band-red) 0%,var(--band-red-light) 50%,var(--band-red) 100%)}
.title-top{font-family:"Oswald",sans-serif;font-weight:700;font-style:italic;color:var(--ink);line-height:1;white-space:nowrap}
.title-top .lit{color:var(--signal-yellow)}
.title-main{font-family:"Oswald",sans-serif;font-weight:700;color:var(--paper);line-height:1;white-space:nowrap;letter-spacing:1px}
.black-panel{background:var(--ink)}
.plug-photo{left:0;top:348px;width:438px;height:312px;background:radial-gradient(ellipse at 45% 45%,#ff9a3c 0%,#e0542a 28%,#6a1a10 58%,#000 85%)}
.features-head{left:0;top:663px;width:308px;height:20px;background:linear-gradient(90deg,#fff 0%,#fff 45%,#222 100%);color:var(--feature-red);font-weight:700;font-size:16px;line-height:20px;padding-left:32px}
.features{left:20px;top:688px;list-style:none}
.features li{font-style:italic;font-size:14px;line-height:19px;white-space:nowrap;position:relative;padding-left:12px;letter-spacing:-.2px}
.features li::before{content:"";position:absolute;left:0;top:6px;border-left:6px solid #fff;border-top:3.5px solid transparent;border-bottom:3.5px solid transparent}
.perk{width:120px;left:312px;text-align:center;font-weight:700;font-size:13px;line-height:13px}
.perk svg{display:block;margin:0 auto 4px}
.cert-badge{left:29px;top:863px;width:57px;height:64px;border:2px solid #ddd;border-radius:8px}
.cert-seal{left:102px;top:862px;width:72px;height:72px;border-radius:50%;border:4px double #ddd}
.model{left:20px;top:932px;width:75px;text-align:center;font-family:"Oswald",sans-serif;font-size:8px}
.usa-mark{left:190px;top:868px;width:110px;text-align:center;font-family:"Oswald",sans-serif;font-weight:700;font-size:13px;line-height:14px;letter-spacing:.5px}
.usa-mark svg{display:block;margin:0 auto 5px}
.length-tag{left:0;top:953px}
.length-text{left:27px;top:958px;color:var(--ink);font-family:"Roboto",sans-serif;font-weight:900;line-height:1;white-space:nowrap}
.length-text .num{font-size:70px;letter-spacing:-2px}
.length-text .unit{font-size:38px}
.info-bar{left:439px;width:294px;height:25px;background:var(--signal-yellow);color:var(--ink);font-family:"Work Sans",sans-serif;font-weight:600;font-size:17px;line-height:25px;text-align:center}
.info-text{left:458px;width:258px;font-family:"Work Sans",sans-serif;font-size:14px;line-height:17.8px;color:var(--paper)}
.page-num{font-family:"Roboto",sans-serif;font-size:30px;color:#333;font-weight:400}
.guide-line{height:1px;background:#bfe6d9}
</style>
</head>
<body>
<div class="sleeve">
  <div class="cord-photo top" role="img" aria-label="Photo of the coiled red extension cord with a white tie"></div>

  <div class="abs silver-band"></div>
  <div class="abs guide-blue" style="top:156px"></div>

  <div class="abs brand" style="left:132px;top:196px"><span class="brand-dot"></span>VOLTLINE</div>
  <div class="abs brand" style="left:483px;top:196px"><span class="brand-dot"></span>VOLTLINE</div>

  <!-- front panel -->
  <div class="abs red-band" style="left:0;top:235px;width:438px;height:113px"></div>
  <div class="abs title-top" style="left:22px;top:254px;font-size:32px">OUTDOOR <span class="lit">LIGHTED</span></div>
  <div class="abs title-main" style="left:22px;top:280px;font-size:53px">EXTENSION CORD</div>

  <div class="abs black-panel" style="left:0;top:348px;width:438px;height:709px"></div>
  <div class="abs plug-photo" role="img" aria-label="Photo of the glowing lighted cord connector"></div>

  <div class="abs features-head">PRODUCT FEATURES</div>
  <ul class="abs features">
    <li>For rugged indoor and outdoor use.</li>
    <li>Unbreakable moisture resistant molded connectors.</li>
    <li>Built in heavy duty strain relief.</li>
    <li>Water and flame resistant.</li>
    <li>Built in power indicator light.</li>
    <li>Safety certified.</li>
    <li>Manufactured to meet OSHA requirements.</li>
    <li>Rated from -40°C (-40°F) to +60°C (+140°F).</li>
  </ul>

  <div class="abs perk" style="top:611px">
    <svg width="40" height="40" viewBox="0 0 40 40"><circle cx="20" cy="20" r="19.5" fill="#fcd006"/><path d="M10 26 L28 14 M12 28 L30 16" stroke="#000" stroke-width="2.2" stroke-linecap="round"/><path d="M28 14 l3-2 M30 16 l3-2" stroke="#000" stroke-width="1.4"/></svg>
    Heavy Copper<br>Wire</div>
  <div class="abs perk" style="top:691px">
    <svg width="40" height="40" viewBox="0 0 40 40"><circle cx="20" cy="20" r="19.5" fill="#fcd006"/><path d="M9 21 L17 14 L17 29 L9 29 Z" fill="#000"/><circle cx="24" cy="19" r="4" fill="none" stroke="#000" stroke-width="2"/><path d="M24 11v3M24 24v3M16 19h-1M29 19h3M29 13l-2 2M29 25l-2-2" stroke="#000" stroke-width="1.6"/></svg>
    Indoor &amp;<br>Outdoor</div>
  <div class="abs perk" style="top:772px">
    <svg width="40" height="40" viewBox="0 0 40 40"><circle cx="20" cy="20" r="19.5" fill="#fcd006"/><path d="M14 25 v-6 a6 6 0 0 1 12 0 v6 Z" fill="none" stroke="#000" stroke-width="2"/><path d="M12 28h16M17 28v3M23 28v3M20 8v3M11 12l2 2M29 12l-2 2" stroke="#000" stroke-width="2"/></svg>
    Indicator Light<br>In Both Ends</div>
  <div class="abs perk" style="top:853px">
    <svg width="40" height="40" viewBox="0 0 40 40"><circle cx="20" cy="20" r="19.5" fill="#fcd006"/><path d="M16 8v5M20 8v5M24 8v5" stroke="#000" stroke-width="2"/><path d="M14 13h12v8l-3 4h-6l-3-4Z" fill="#000"/><path d="M20 25v8" stroke="#000" stroke-width="3"/></svg>
    Heavy Duty<br>Strain Relief</div>
  <div class="abs perk" style="top:939px">
    <svg width="40" height="40" viewBox="0 0 40 40"><circle cx="20" cy="20" r="19.5" fill="#fcd006"/><path d="M20 9 C24 15 27 18 27 23 a7 7 0 0 1-14 0 c0-4 3-6 4-9 c1 3 2 4 3 4 c0-3-1-6 0-9Z" fill="#000"/></svg>
    Water &amp; Flame<br>Resistant</div>

  <div class="abs cert-badge"></div>
  <div class="abs cert-seal"></div>
  <div class="abs model">VC-12S025-R</div>

  <div class="abs usa-mark">
    <svg width="54" height="30" viewBox="0 0 57 30" aria-label="American flag">
      <rect width="57" height="30" fill="#fff"/>
      <g fill="var(--flag-red)">
        <rect y="0" width="57" height="2.31"/><rect y="4.62" width="57" height="2.31"/><rect y="9.23" width="57" height="2.31"/><rect y="13.85" width="57" height="2.31"/><rect y="18.46" width="57" height="2.31"/><rect y="23.08" width="57" height="2.31"/><rect y="27.69" width="57" height="2.31"/>
      </g>
      <rect width="23" height="16.15" fill="var(--flag-blue)"/>
      <g fill="#fff">
        <circle cx="4" cy="3.5" r=".9"/><circle cx="9" cy="3.5" r=".9"/><circle cx="14" cy="3.5" r=".9"/><circle cx="19" cy="3.5" r=".9"/>
        <circle cx="6.5" cy="8" r=".9"/><circle cx="11.5" cy="8" r=".9"/><circle cx="16.5" cy="8" r=".9"/>
        <circle cx="4" cy="12.5" r=".9"/><circle cx="9" cy="12.5" r=".9"/><circle cx="14" cy="12.5" r=".9"/><circle cx="19" cy="12.5" r=".9"/>
      </g>
    </svg>
    MADE IN<br>THE USA</div>

  <svg class="abs length-tag" width="200" height="95" viewBox="0 0 200 95"><path d="M0 0H172L196 47L172 95H0Z" fill="#fcd006"/></svg>
  <div class="abs length-text"><span class="num">25</span><span class="unit">FT</span></div>

  <!-- back panel -->
  <div class="abs red-band" style="left:439px;top:235px;width:294px;height:83px"></div>
  <div class="abs title-top" style="left:458px;top:251px;font-size:21px">OUTDOOR <span class="lit">LIGHTED</span></div>
  <div class="abs title-main" style="left:458px;top:268px;font-size:35px">EXTENSION CORD</div>
  <div class="abs" style="left:439px;top:318px;width:294px;height:4px;background:#ddd"></div>
  <div class="abs black-panel" style="left:439px;top:322px;width:294px;height:735px"></div>

  <div class="abs info-bar" style="top:352px">For Your Protection</div>
  <p class="abs info-text" style="top:388px">Store indoors when not in use. &nbsp;Always uncoil cord before use. Keep out of reach of children. Always turn off appliance prior to plugging into power source. Always grasp the plug, not the cord, when plugging and unplugging cord.</p>

  <div class="abs info-bar" style="top:535px;left:434px;width:299px">Caution</div>
  <p class="abs info-text" style="top:567px">Inspect cable prior to each use for cracks, loose connectors or bare conductors. Do not ever use any faulty or damaged cable. Do not repair, splice or modify this product in any way. Do not exceed the electrical rating of this product. Protect cord connection points from water or wet conditions.<br>Unplug cord when not in use.</p>

  <div class="abs info-bar" style="top:747px">Warning</div>
  <p class="abs info-text" style="top:780px;width:264px">Failure to properly use this product could result in fire, serious or fatal injury.</p>

  <div class="abs info-bar" style="top:835px">Warranty</div>
  <p class="abs info-text" style="top:869px">For the lifetime of this product,<br>if it fails due to a manufacturing defect, return it to Coilmark Wire for a free replacement. This warranty is limited to the replacement of the product only and no other warranty, liability, or responsibility is implied or<br>expressed.</p>

  <div class="abs guide-fold" style="top:156px;height:877px"></div>
  <div class="abs guide-blue" style="top:1032px"></div>

  <div class="cord-photo bottom" role="img" aria-label="Photo of the coiled red extension cord with its lighted plug end"></div>

  <div class="abs guide-line" style="left:0;top:1146px;width:200px"></div>
  <div class="abs guide-line" style="left:235px;top:1146px;width:200px"></div>
  <div class="abs guide-line" style="left:440px;top:1146px;width:125px"></div>
  <div class="abs guide-line" style="left:605px;top:1146px;width:128px"></div>
  <div class="abs page-num" style="left:211px;top:1126px">3</div>
  <div class="abs page-num" style="left:576px;top:1126px">2</div>
</div>
</body>
</html>
```